A4 Flyer Design outlining our financial philosophy

One A4 page design (landscape orientation) outlining our financial philosophy.
The design needs to show these steps as the building blocks and the path taken to financial success:
1. Maximise income and reduce expenses
2. Maximise savings and reduce bad debts
3. Invest wisely & tax effectively
4. Manage risk
5. Plan for retirement
6. Leave a legacy
The design needs to incorporate the 6 building blocks above along with the key points for each topic. More info attached.
Design must be engaging, professional and consistent with our current branding colours.

Target Market(s)

self employed individuals looking to build wealth through property and shares.

Industry/Entity Type

Financial Planning

Font styles to use
Sans Serif

Colors
0255a3
5c5c5c
000000
ffffff

Requirements
Must have
• clear and engaging.
• consistent with current branding
• 6 topics with key considerations (as per attached)
• must show that all 6 points are linked and are a journey.

```html
<!DOCTYPE html>
<html lang="en">
<head>
<meta charset="utf-8">
<title>The 6 Building Blocks to Financial Success</title>
<link href="https://fonts.googleapis.com/css2?family=Open+Sans:wght@300;400;600;700;800&display=swap" rel="stylesheet">
<style>
  :root {
    --brand-navy: #1f3f86;
    --page-bg: #f7f7f7;
    --white: #ffffff;
    --teal: #6dcde0;
    --teal-side: #19b1ca;
    --teal-dark: #128ea3;
    --sage: #6f8a85;
    --sage-side: #394a47;
    --sage-dark: #2b3735;
    --coral: #f0695a;
    --coral-side: #e2412f;
    --coral-dark: #b93424;
    --slate: #4b6a7c;
    --slate-side: #2c4455;
    --slate-dark: #1f3240;
    --brand-name: #1f3f86;
    --logo-panel: #e9eaec;
  }
  * { box-sizing: border-box; margin: 0; padding: 0; }
  html, body { width: 1200px; height: 849px; overflow: hidden; }
  body { background: var(--page-bg); font-family: "Open Sans", Arial, sans-serif; }
  .flyer { position: relative; width: 1200px; height: 849px; background: var(--page-bg); overflow: hidden; }

  .masthead {
    position: absolute; left: 0; top: 0; width: 1200px; height: 100px;
    background: var(--brand-navy);
    display: flex; align-items: center; justify-content: center;
  }
  .masthead h1 {
    color: var(--white); font-weight: 800; font-size: 41.5px; letter-spacing: 0;
    text-transform: uppercase; line-height: 1;
  }

  .step {
    position: absolute; left: 136px; width: 672px;
    display: flex; align-items: center; color: var(--white);
  }
  .step--teal { background: var(--teal); }
  .step--sage { background: var(--sage); }
  .step--coral { background: var(--coral); }
  .step--slate { background: var(--slate); }

  .step__number { width: 96px; text-align: center; font-size: 31px; font-weight: 400; }
  .step__title {
    width: 273px; font-size: 17px; font-weight: 600; text-transform: uppercase;
    letter-spacing: 0.3px; line-height: 1.45;
  }
  .step__points { list-style: none; width: 272px; font-size: 8.6px; line-height: 1.35; }
  .step__points li::before { content: "\2022\00a0"; }

  .stack { position: absolute; left: 796px; top: 116px; }

  .ladder {
    position: absolute; left: 932px; top: 172px; width: 135px; height: 535px;
  }

  .brand {
    position: absolute; left: 932px; top: 737px; width: 210px; height: 71px;
    background: var(--logo-panel);
    display: flex; align-items: center; gap: 10px; padding-left: 10px;
  }
  .brand__dot { width: 40px; height: 40px; border-radius: 50%; background: var(--brand-name); flex: none; }
  .brand__name {
    color: var(--brand-name); font-weight: 700; font-size: 14px; line-height: 1.2;
    letter-spacing: 0.4px; text-transform: uppercase;
  }
</style>
</head>
<body>
<main class="flyer">
  <header class="masthead">
    <h1>The 6 Building Blocks to Financial Success</h1>
  </header>

  <svg class="stack" width="260" height="610" viewBox="820 120 260 610" aria-hidden="true">
    <g transform="translate(-2,0)">
    <polygon points="830,164 905,136 1060,265 1060,300 905,257 830,257" fill="var(--teal-side)"/>
    <polygon points="830,164 905,136 905,257 830,257" fill="var(--teal-dark)"/>
    <polygon points="905,235 1060,300 1060,380 905,358" fill="var(--sage-dark)"/>
    <polygon points="830,265 905,235 905,358 830,358" fill="var(--sage-side)"/>
    <polygon points="905,345 1060,385 1060,445 905,432" fill="var(--coral-dark)"/>
    <polygon points="830,366 905,345 905,432 830,432" fill="var(--coral-side)"/>
    <polygon points="905,424 1060,440 1060,540 905,526" fill="var(--slate-dark)"/>
    <polygon points="830,439 905,424 905,526 830,526" fill="var(--slate-side)"/>
    <polygon points="905,524 1060,532 1060,615 905,612" fill="var(--teal-dark)"/>
    <polygon points="830,533 905,524 905,612 830,612" fill="var(--teal-side)"/>
    <polygon points="905,618 1060,618 1060,690 905,727" fill="var(--sage-dark)"/>
    <polygon points="830,620 905,618 905,727 830,707" fill="var(--sage-side)"/>

    <g fill="none" stroke="var(--white)" stroke-width="3" stroke-linecap="round" stroke-linejoin="round">
      <path d="M858 186 h20 v8 a10 10 0 0 1 -20 0 z" fill="var(--white)"/>
      <path d="M858 190 h-5 a5 5 0 0 0 6 8 M878 190 h5 a5 5 0 0 1 -6 8"/>
      <path d="M868 204 v8 M861 214 h14"/>
      <path d="M858 286 v20 h16 M858 306 l-3 5 M874 306 l4 5 M852 312 q14 5 30 -2"/>
      <circle cx="870" cy="286" r="4" fill="var(--white)"/>
      <path d="M868 372 l13 5 v9 q0 10 -13 16 q-13 -6 -13 -16 v-9 z" fill="var(--white)" stroke="none"/>
      <path d="M863 387 l4 4 l8 -8" stroke="var(--coral-side)"/>
      <path d="M851 470 v20 h32"/>
      <path d="M856 482 l8 -7 l6 4 l11 -12 M877 467 h4 v4"/>
      <circle cx="866" cy="545" r="6"/>
      <ellipse cx="868" cy="571" rx="14" ry="10" fill="var(--white)" stroke="none"/>
      <path d="M860 580 v4 M875 580 v4"/>
      <circle cx="864" cy="660" r="12"/>
      <path d="M868 654 h-6 a3 3 0 0 0 0 6 h4 a3 3 0 0 1 0 6 h-6 M864 651 v18"/>
      <path d="M874 670 l6 -6 l6 6 M880 664 v14"/>
    </g>
    </g>
  </svg>

  <svg class="ladder" viewBox="0 0 150 560" preserveAspectRatio="none" role="img" aria-label="Ladder leaning against the stacked blocks, showing the climb from step 1 to step 6">
    <defs>
      <linearGradient id="ladderTone" x1="0" x2="1">
        <stop offset="0" stop-color="#ffffff"/>
        <stop offset="1" stop-color="#d9dcde"/>
      </linearGradient>
    </defs>
    <polygon points="0,0 30,0 150,540 110,545" fill="url(#ladderTone)" opacity="0.92"/>
  </svg>

  <section class="step step--teal" style="top:160px;height:90px;">
    <span class="step__number">6</span>
    <h2 class="step__title">Leave a Legacy</h2>
    <ul class="step__points">
      <li>Having a Will</li>
      <li>Power of Attorney</li>
      <li>Testamentary Trust?</li>
      <li>Guardianship</li>
    </ul>
  </section>

  <section class="step step--sage" style="top:258px;height:90px;">
    <span class="step__number">5</span>
    <h2 class="step__title">Plan for Retirement</h2>
    <ul class="step__points">
      <li>Replacement of your salary or profits from running a business with income from your investment portfolio</li>
      <li>Drawing a sustainable income to maintain a great lifestyle and protect your retirement nest egg</li>
    </ul>
  </section>

  <section class="step step--coral" style="top:356px;height:64px;">
    <span class="step__number">4</span>
    <h2 class="step__title">Manage Risk</h2>
    <ul class="step__points">
      <li>Insurance</li>
      <li>Contingency plans</li>
      <li>Diversification</li>
      <li>Focus on quality</li>
    </ul>
  </section>

  <section class="step step--slate" style="top:427px;height:85px;">
    <span class="step__number">3</span>
    <h2 class="step__title">Invest Wisely<br>and Tax Effectively</h2>
    <ul class="step__points" style="width:300px;">
      <li>Build an investment portfolio e.g. property and shares</li>
      <li>Use appropriate tax structures such as Family Trusts / Superannuation</li>
      <li>Invest for Growth or Income?</li>
      <li>Timing of tax deductions</li>
      <li>Depreciation</li>
    </ul>
  </section>

  <section class="step step--teal" style="top:519px;height:77px;">
    <span class="step__number">2</span>
    <h2 class="step__title">Maximise Savings<br>and Reduce Bad Debts</h2>
    <ul class="step__points" style="width:300px;">
      <li>Surplus income increases savings and equity</li>
      <li>Use savings and equity for investments</li>
      <li>Avoid borrowing for lifestyle assets/experiences where possible</li>
    </ul>
  </section>

  <section class="step step--sage" style="top:603px;height:85px;">
    <span class="step__number">1</span>
    <h2 class="step__title">Maximise Income<br>and Reduce Expenses</h2>
    <ul class="step__points">
      <li>Invest in yourself through education and training</li>
      <li>Build a number of income streams</li>
      <li>Align your spending with your values</li>
      <li>Track your spending</li>
      <li>Increase surplus income</li>
    </ul>
  </section>

  <footer class="brand">
    <span class="brand__dot"></span>
    <span class="brand__name">Quenvarro<br>Ledgerfield</span>
  </footer>
</main>
</body>
</html>
```